Website Design for Quellbrook.Com

Quellbrook.com is being launched as a site that enables and fosters communications between individuals affected by, or interested in, disasters and crises. The domain has been owned since 1992 and we feel it's time to give back to the Internet community.

```html
<!DOCTYPE html>
<html lang="en">
<head>
<meta charset="utf-8">
<title>Quellbrook.com — people supporting people</title>
<link rel="stylesheet" href="https://fonts.googleapis.com/css2?family=Open+Sans:wght@400;600;700&family=Oswald:wght@400;600&display=swap">
<style>
:root{
  --green:#2f9a5c;
  --green-light:#3fb46f;
  --orange:#e84c22;
  --orange-text:#d9461d;
  --navy:#1f2b45;
  --charcoal:#1b1b1b;
  --ink:#2b2b2b;
  --white:#ffffff;
  --ad-light:#cfcfcf;
  --ad-dark:#686868;
}
*{box-sizing:border-box;margin:0;padding:0}
html,body{width:1200px;height:872px;overflow:hidden}
body{font-family:"Open Sans",Arial,sans-serif;color:var(--ink);background:var(--charcoal);position:relative}
.canvas{position:absolute;inset:0;overflow:hidden;
  background:linear-gradient(180deg,#1e1e1e 0,#2a2a2a 150px,#151515 500px,#222 640px,#9a9a9a 760px,#e4e4e4 872px)}
.paper-band{position:absolute;left:0;top:0;width:1200px;height:520px}
.abs{position:absolute}

/* header */
.brand{left:233px;top:16px}
.brand-name{font-weight:700;font-size:44px;color:var(--green);letter-spacing:-1px;line-height:1}
.brand-name small{font-size:15px;letter-spacing:0;vertical-align:top;margin-left:2px}
.brand-tag{font-size:16px;color:#cfcfcf;margin-top:2px}
.date{left:583px;top:17px;font-size:11px;color:var(--green-light);white-space:nowrap}
.social{left:736px;top:15px;display:flex;gap:7px;align-items:center;white-space:nowrap}
.pill{display:flex;align-items:center;gap:3px;font-size:9.5px}
.pill .ic{width:14px;height:14px;background:var(--orange);border-radius:50%}
.pill .ic.sq{border-radius:2px;background:#3b5b99}
.pill .ic.sq2{border-radius:2px;background:#5aa7dd}
.pill .lbl{background:#eee;color:#333;padding:0 4px;border-radius:2px}
.pill .cnt{background:#fff;color:#444;padding:0 4px;border:1px solid #aaa;border-radius:2px}
.rss{width:12px;height:12px;background:#f29a1d;border-radius:2px}
.nav{left:553px;top:43px;display:flex;font-size:11px;color:var(--white);white-space:nowrap}
.nav a{color:inherit;text-decoration:none;padding:0 7px;border-left:1px solid #bbb;line-height:12px}
.nav a:first-child{border-left:0}
.search{left:695px;top:66px;width:174px;height:14px;border-radius:3px;background:#1d5a36;border:1px solid var(--green);font-size:8px;color:#9fd9b5;padding-left:6px;line-height:12px}
.account{left:883px;top:65px;font-size:11px;color:var(--orange);font-weight:600;white-space:nowrap}

/* slider */
.photo-back{left:170px;top:128px;width:180px;height:345px;background:#fff;transform:rotate(-4deg);box-shadow:0 3px 10px rgba(0,0,0,.5)}
.photo-back .img{position:absolute;inset:10px;background:linear-gradient(160deg,#a99a86,#6f655a)}
.photo-main{left:228px;top:113px;width:420px;height:348px;background:#fff;padding:12px;transform:rotate(2deg);box-shadow:0 4px 14px rgba(0,0,0,.5)}
.photo-main .img{width:100%;height:100%;background:linear-gradient(170deg,#9fc3e0 0,#c7c2b6 22%,#a9a49a 55%,#77716a 100%)}
.arrow{width:34px;height:34px;border-radius:50%;background:rgba(47,154,92,.85)}
.arrow svg{display:block}

/* right column */
.side{left:695px;top:172px;width:278px}
.sec-title{font-family:"Oswald",Arial,sans-serif;font-size:12px;color:var(--orange-text);letter-spacing:.2px;white-space:nowrap}
.sec-title.big{font-size:13.5px}
.body-s{font-size:9.5px;color:#333;line-height:12px}
.meta{font-size:10px;color:var(--green);margin-top:8px}
.rule{height:1px;background:#8d8d8d;margin:7px 0}
.row{display:flex;align-items:center;justify-content:space-between}
.thumbs{display:flex;gap:3px}
.thumbs span{width:25px;height:22px;background:linear-gradient(135deg,#7c756b,#3f3a35)}
.appeals{display:flex;gap:10px}
.appeals-head{width:60px;flex:none}
.appeals-head b{font-family:"Oswald",Arial,sans-serif;font-weight:400;font-size:14px;color:var(--green)}
.appeals-head i{display:block;font-style:normal;font-size:9px}
.appeals-body{border-left:3px solid #555;padding-left:6px;flex:1}
.appeals-body em{font-style:normal;color:var(--orange-text);font-weight:600}
.killed{display:flex;gap:10px;align-items:flex-start}
.killed-num{font-family:"Oswald",Arial,sans-serif;color:var(--orange-text);text-align:center;line-height:1}
.killed-num b{font-size:36px;font-weight:600;display:block}
.killed-num span{font-size:11px;color:#333}
.killed-title{font-size:12px;font-weight:700;color:var(--green);white-space:nowrap}
.more{margin-left:auto;display:block;width:64px;background:var(--orange);color:#fff;font-size:9px;text-align:center;padding:2px 0;margin-top:5px}
.weather{display:flex;height:42px;background:var(--navy);color:#fff;margin-top:8px;white-space:nowrap}
.weather-now{display:flex;align-items:center;gap:6px;padding:0 8px;border-right:1px solid #56617b;width:166px;flex:none}
.weather-now b{font-size:22px;font-weight:400;line-height:1}
.weather-now small{font-size:10px;line-height:12px}
.weather-now small i{color:var(--orange);font-style:normal;font-size:9px}
.weather-world{position:relative;flex:1;font-size:9.5px;padding:8px 6px;line-height:11px}
.weather-world .go{position:absolute;right:3px;bottom:3px;width:22px;height:18px;background:var(--orange)}

/* feature card */
.dot-map{left:192px;top:495px;width:196px;height:150px;border-radius:40% 50% 45% 55%;background:radial-gradient(circle at 40% 40%,rgba(40,70,100,.55),rgba(20,35,50,0) 70%)}
.connector{left:340px;top:537px;width:56px;height:2px;background:var(--green)}
.connector-dot{left:337px;top:533px;width:11px;height:11px;border-radius:50%;background:var(--green)}
.feature{left:393px;top:500px;width:587px;height:118px;background:var(--orange);box-shadow:0 3px 8px rgba(0,0,0,.5)}
.feature-thumb{position:absolute;left:10px;top:9px;width:101px;height:101px;background:#6a6a6a}
.feature-title{position:absolute;left:125px;top:6px;font-size:16px;color:#fff;font-weight:400}
.feature-text{position:absolute;left:125px;top:32px;width:420px;font-size:10px;color:#fff;line-height:12.5px}
.share{position:absolute;right:14px;bottom:8px;display:flex;gap:5px}
.share span{width:18px;height:18px;background:#3e6aa6;border-radius:2px}
.share span:last-child{background:#65b1e6}

/* lower page */
.page{left:220px;top:637px;width:760px;height:235px;background:#f5f5f5}
.ad-left{left:220px;top:639px;width:184px;height:72px;background:var(--ad-light);text-align:center;font-size:9.5px;color:#222;padding-top:14px;line-height:11px}
.ad-left strong{display:block;font-size:19px;color:#333;line-height:20px}
.ad-left em{font-style:normal;color:#fff}
.ad-slot{left:404px;top:639px;width:576px;height:72px;background:var(--ad-dark);color:#ddd;font-size:9px;display:flex;align-items:center;justify-content:center}
.gallery{left:220px;top:720px;display:flex;gap:8px}
.gallery div{width:184px;height:121px}
.g1{background:linear-gradient(160deg,#3a1a08,#c9520e 55%,#f0a02a)}
.g2{background:linear-gradient(170deg,#8f8a76,#6e6a58 50%,#4e5546)}
.g3{background:linear-gradient(170deg,#5a4a40,#c14a1e 45%,#2c3540)}
.g4{background:linear-gradient(165deg,#bfb7a8,#8b8274 60%,#5f584f)}
.forum-title{left:220px;top:851px;font-size:16px;font-weight:400;color:var(--orange-text);white-space:nowrap}
.pager{left:607px;top:857px;display:flex;gap:3px;font-size:9px}
.pager span{width:13px;height:13px;background:#555;color:#fff;text-align:center;line-height:13px}
.pager a{color:var(--green);margin-left:8px;line-height:9px;font-size:8.5px}
.side-box{left:780px;top:853px;width:200px;height:19px;background:#666}
</style>
</head>
<body>
<div class="canvas">

  <svg class="paper-band" viewBox="0 0 1200 520" aria-hidden="true">
    <defs>
      <linearGradient id="paperFill" x1="0" y1="0" x2="0" y2="1">
        <stop offset="0" stop-color="#d4d4d4"/>
        <stop offset="1" stop-color="#a8a8a8"/>
      </linearGradient>
    </defs>
    <path d="M0 165 L60 150 L140 160 L230 140 L330 150 L520 128 L620 118 L700 132 L800 110 L900 122 L1000 104 L1100 118 L1200 100 L1200 470 L1120 458 L1040 470 L980 460 L880 476 L780 468 L700 480 L560 470 L440 484 L330 476 L220 492 L120 500 L0 512 Z" fill="url(#paperFill)"/>
    <path d="M0 165 L60 150 L140 160 L230 140 L330 150 L520 128 L620 118 L700 132 L800 110 L900 122 L1000 104 L1100 118 L1200 100" fill="none" stroke="#f2f2f2" stroke-width="4"/>
    <path d="M0 512 L120 500 L220 492 L330 476 L440 484" fill="none" stroke="#eeeeee" stroke-width="3"/>
  </svg>

  <header>
    <div class="abs brand">
      <div class="brand-name">Quellbrook<small>.com</small></div>
      <div class="brand-tag">people supporting people</div>
    </div>
    <div class="abs date">Saturday, February 16, 2013</div>
    <div class="abs social">
      <div class="pill"><span class="ic"></span><span class="cnt">33K</span></div>
      <div class="pill"><span class="ic sq"></span><span class="lbl">Share</span><span class="cnt">3.8k</span></div>
      <div class="pill"><span class="ic sq2"></span><span class="lbl">Post</span><span class="cnt">2,535</span></div>
      <span class="rss"></span>
    </div>
    <nav class="abs nav">
      <a href="#">Home</a><a href="#">Forums</a><a href="#">Resources</a><a href="#">Store</a><a href="#">Online Chat</a><a href="#">Gallery</a><a href="#">About Us</a><a href="#">Contact Us</a>
    </nav>
    <div class="abs search">SEARCH</div>
    <div class="abs account">REGISTER &nbsp;|&nbsp; LOGIN</div>
  </header>

  <section class="slider">
    <div class="abs photo-back"><div class="img" role="img" aria-label="Photo of a disaster scene"></div></div>
    <div class="abs photo-main"><div class="img" role="img" aria-label="Photo of rescuers searching a collapsed building"></div></div>
    <div class="abs arrow" style="left:197px;top:281px"><svg width="34" height="34"><path d="M20 10 L13 17 L20 24" stroke="#fff" stroke-width="3" fill="none"/></svg></div>
    <div class="abs arrow" style="left:628px;top:281px"><svg width="34" height="34"><path d="M14 10 L21 17 L14 24" stroke="#fff" stroke-width="3" fill="none"/></svg></div>
  </section>

  <aside class="abs side">
    <div class="sec-title">WORLD / COUNTRY UPDATES <span style="display:inline-block;width:12px;height:12px;background:#555;vertical-align:middle"></span></div>
    <p class="body-s">It is a long established fact that a reader will be distracted by the readable content of a page when looking at its layout.</p>
    <div class="meta">Country Name | 16-02-2013 | Storm</div>
    <div class="rule"></div>
    <div class="row">
      <div class="sec-title big">DISASTER HIGHLIGHTS / STORY</div>
      <div class="thumbs" role="img" aria-label="Story thumbnails"><span></span><span></span><span></span></div>
    </div>
    <div class="rule"></div>
    <div class="appeals">
      <div class="appeals-head"><b>APPEALS</b><i>15 Feb 2013</i></div>
      <p class="body-s appeals-body"><em>It is a long established fact that</em> a reader will be distracted by the readable content of a page when looking at its layout. The point of using Lorem Ipsum is that it has a more-or-less normal distribution of letters</p>
    </div>
    <div class="rule"></div>
    <div class="killed">
      <div class="killed-num"><b>21</b><span>KILLED</span></div>
      <div style="flex:1;padding-top:3px">
        <div class="killed-title">150 injured in Haiti earthquake</div>
        <p class="body-s">There are many variations of passages of Lorem</p>
        <span class="more">more detail</span>
      </div>
    </div>
    <div class="weather">
      <div class="weather-now">
        <svg width="26" height="24" aria-hidden="true"><ellipse cx="13" cy="10" rx="10" ry="7" fill="#dfe6f2"/><path d="M7 19 l-2 4 M13 19 l-2 4 M19 19 l-2 4" stroke="#8fb6e8" stroke-width="2"/></svg>
        <b>36°&nbsp;F</b>
        <small>City Name<br><i>47° / 33°</i></small>
      </div>
      <div class="weather-world">WEATHER AROUND<br>THE WORLD<span class="go"></span></div>
    </div>
  </aside>

  <section class="feature-wrap">
    <div class="abs dot-map" role="img" aria-label="Dotted world map decoration"></div>
    <div class="abs connector"></div>
    <div class="abs connector-dot"></div>
    <article class="abs feature">
      <div class="feature-thumb" role="img" aria-label="Feature story image"></div>
      <h2 class="feature-title">Disaster</h2>
      <p class="feature-text">There are many variations of passages of Lorem Ipsum available, but the majority have suffered alteration in some form, by injected humour, or randomised words which don't look even slightly believable. If you are going to use a passage of Lorem Ipsum,</p>
      <div class="share"><span></span><span></span><span></span></div>
    </article>
  </section>

  <main>
    <div class="abs page"></div>
    <div class="abs ad-left">Click here for advertisement on<strong>Quellbrook</strong>Read our <em>privacy policy</em></div>
    <div class="abs ad-slot">AD</div>
    <div class="abs gallery">
      <div class="g1" role="img" aria-label="Photo of a house on fire"></div>
      <div class="g2" role="img" aria-label="Photo of a flooded street"></div>
      <div class="g3" role="img" aria-label="Photo of a burning ship"></div>
      <div class="g4" role="img" aria-label="Photo of earthquake rubble"></div>
    </div>
    <h3 class="abs forum-title">Forum Discussion</h3>
    <div class="abs pager"><span>1</span><span>2</span><span>3</span><span>4</span><a href="#">see all<br>discussions</a></div>
    <div class="abs side-box"></div>
  </main>

</div>
</body>
</html>
```